Medical Company in need of Modern business card design for new Wound Care clinic.

Modern business card design for our Woundcare company. Logo and description of services can be found on our website; https://www.tovrel-woundcare.com/

```html
<!DOCTYPE html>
<html lang="en">
<head>
<meta charset="utf-8">
<title>Tovrel Woundcare – Business Card</title>
<link href="https://fonts.googleapis.com/css2?family=Montserrat:wght@400;500&family=Arimo:wght@400;700&display=swap" rel="stylesheet">
<style>
  :root {
    --backdrop: #2b2b2b;
    --card-light: #ffffff;
    --card-dark: #333333;
    --ink: #1a1a1a;
    --gold: #c9923a;
    --text-light: #f2f2f2;
    --mark-faint: #3b3b3b;
  }
  * { box-sizing: border-box; margin: 0; padding: 0; }
  html, body { width: 1200px; height: 689px; overflow: hidden; }
  body {
    background: var(--backdrop);
    display: flex;
    align-items: center;
    justify-content: center;
    gap: 48px;
    font-family: "Arimo", Arial, sans-serif;
  }
  .card {
    width: 520px;
    height: 297px;
    border-radius: 18px;
    position: relative;
    overflow: hidden;
  }
  .card--front {
    background: var(--card-light);
    display: flex;
    align-items: center;
    justify-content: center;
    gap: 14px;
  }
  .brand-dot {
    width: 16px;
    height: 16px;
    background: var(--gold);
  }
  .wordmark {
    font-family: "Montserrat", Arial, sans-serif;
    font-weight: 400;
    letter-spacing: 0.32em;
    text-transform: uppercase;
    white-space: nowrap;
  }
  .card--front .wordmark { color: var(--ink); font-size: 24px; }
  .card--back { background: var(--card-dark); padding: 40px 40px; }
  .card--back .wordmark {
    position: relative;
    z-index: 1;
    color: var(--gold);
    font-size: 20px;
    margin-bottom: 24px;
  }
  .back-details { position: relative; z-index: 1; }
  .holder-name { color: var(--gold); font-weight: 700; font-size: 22px; }
  .holder-role { color: var(--text-light); font-size: 13px; margin-bottom: 14px; }
  .address { color: var(--text-light); font-size: 13px; line-height: 1.35; margin-bottom: 14px; font-style: normal; }
  .contacts { list-style: none; color: var(--text-light); font-size: 13px; line-height: 1.45; }
  .contacts li { display: flex; align-items: center; gap: 10px; }
  .contacts svg { width: 11px; height: 11px; flex: none; }
  .faint-square {
    position: absolute;
    right: 48px;
    top: 104px;
    width: 130px;
    height: 130px;
    background: var(--mark-faint);
  }
</style>
</head>
<body>
  <section class="card card--front">
    <span class="brand-dot"></span>
    <span class="wordmark">Tovrel Woundcare</span>
  </section>

  <section class="card card--back">
    <div class="faint-square"></div>
    <div class="wordmark">Tovrel Woundcare</div>
    <div class="back-details">
      <div class="holder-name">Daniel Reyes</div>
      <div class="holder-role">President</div>
      <address class="address">
        1820 Corvane Ave, Ste 210<br>
        PMB 48217 Dallas<br>
        TX 75240
      </address>
      <ul class="contacts">
        <li>
          <svg viewBox="0 0 24 24"><path fill="var(--gold)" d="M6.6 10.8a15.1 15.1 0 0 0 6.6 6.6l2.2-2.2a1 1 0 0 1 1-.25 11.4 11.4 0 0 0 3.6.57 1 1 0 0 1 1 1V20a1 1 0 0 1-1 1A17 17 0 0 1 3 4a1 1 0 0 1 1-1h3.5a1 1 0 0 1 1 1c0 1.25.2 2.45.57 3.57a1 1 0 0 1-.25 1z"/></svg>
          972-555-0143
        </li>
        <li>
          <svg viewBox="0 0 24 24"><rect x="2" y="5" width="20" height="14" fill="var(--gold)"/><path d="M2 5l10 8 10-8" fill="none" stroke="var(--card-dark)" stroke-width="2"/></svg>
          info@tovrel-woundcare.com
        </li>
        <li>
          <svg viewBox="0 0 24 24"><circle cx="12" cy="12" r="10" fill="none" stroke="var(--gold)" stroke-width="2.5"/><path d="M2 12h20M12 2c3 3 3 17 0 20M12 2c-3 3-3 17 0 20" fill="none" stroke="var(--gold)" stroke-width="2"/></svg>
          www.tovrel-woundcare.com
        </li>
      </ul>
    </div>
  </section>
</body>
</html>
```